Labels for new organic cosmetics/personal care brand called Venoro

I need labels for new cosmetic brand named ( Venoro )
It is natural and organic
products include:
**natural soaps 3 in a box ( 7 types): shea butter soap, almond soap, lavender soap, apricot soap, olive soap , camel milk soap and sensitive skin soap.

**Organic shea butters (7 types) (in round container) pure shea butter, Shea butter with argan oil, shea butter with olive oil, shea butter with oats, Shea butter with camel milk, shea butter with camel milk and Agarwood and shea butter with donky milk.

**deodorant: one type only , a crystal deodorant.

**shampoo (in cylindrical container) : one type natural shampoo

** Organic Oils (two types) (in clyndrical container) : Argan oil and Rose hip oil.

attached examples of similar containers and outline of labels that i want to have new ones.
**notice:
shape of shea butter container is round and flat.
shape of shampoo is cylindrical.
shape of soaps is a cuboid box.

Target Market(s)

men and women of all ages

Industry/Entity Type

Cosmetics

Font styles to use
Sans Serif

Colors
e4daeb
f9d9e8
fbd4d5
fee3d5
fce8d3
fff3d1
fdf9cf
cee9f5
cadf82

Requirements
Must have
• * Venoro logo
• * organic/natural theme
• * front and back labels
• * 7 labels for soaps, 7 back and 7 front labels for shea butter, one label for deoderant, one label for shampoo, two labels for natural oils.
Nice to have
• leaves, green colors or natural shades of colors , pastel colors
• the color is not specified
Should not have
• **I don't need the container design** .
• just the labels. attached are outline example of the labels and photos of the products so you know the shape of container.
• shape of shea butter container is round and flat.
• shape of shampoo is cylindrical.
• shape of soaps is a cuboid box.

```html
<!DOCTYPE html>
<html lang="en">
<head>
<meta charset="utf-8">
<title>Venoro Organic Shampoo Labels</title>
<link rel="stylesheet" href="https://fonts.googleapis.com/css2?family=Marcellus&family=Arapey&family=Poiret+One&family=Open+Sans:ital,wght@0,400;0,600;1,400&display=swap">
<style>
  :root {
    --page: #ffffff;
    --label: #ffffff;
    --label-edge: #e2e2e2;
    --brand-pink: #c8175d;
    --brand-dot: #7fb52d;
    --ink-grey: #5a5a5a;
    --ink-dark: #3b3b3b;
    --ink-soft: #8a8a8a;
    --rule: #c9c9c9;
    --leaf-green: #5f9a1c;
    --leaf-light: #a9cf3c;
    --leaf-dark: #2f7a23;
  }
  html, body {
    margin: 0;
    padding: 0;
    width: 1200px;
    height: 1200px;
    overflow: hidden;
    background: var(--page);
  }
  h1, p { margin: 0; font-weight: 400; }
  .canvas {
    position: relative;
    width: 1200px;
    height: 1200px;
  }
  .label {
    position: absolute;
    top: 100px;
    width: 392px;
    height: 1000px;
    background: var(--label);
    box-shadow: 0 0 0 1px var(--label-edge), 0 6px 18px rgba(0,0,0,0.08);
    overflow: hidden;
  }
  .label--classic { left: 150px; }
  .label--fresh { left: 658px; }

  .brand {
    position: absolute;
    top: 96px;
    display: flex;
    align-items: center;
    gap: 10px;
    font-family: "Open Sans", sans-serif;
    font-size: 42px;
    color: var(--brand-pink);
    line-height: 1;
  }
  .label--classic .brand { left: 34px; }
  .label--fresh .brand { left: 48px; }
  .brand-dot {
    width: 22px;
    height: 22px;
    border-radius: 50%;
    background: var(--brand-dot);
  }

  .rule {
    position: absolute;
    top: 294px;
    height: 2px;
    background: var(--rule);
  }
  .label--classic .rule { left: 28px; right: 24px; }
  .label--fresh .rule { left: 30px; right: 30px; }

  /* classic label */
  .classic-title {
    position: absolute;
    left: 26px;
    top: 222px;
    font-family: "Marcellus", serif;
    font-size: 62px;
    letter-spacing: 1px;
    color: var(--ink-grey);
    line-height: 1;
  }
  .classic-sub {
    position: absolute;
    left: 30px;
    top: 310px;
    font-family: "Marcellus", serif;
    font-size: 38px;
    color: var(--ink-grey);
    line-height: 1;
  }
  .classic-claim {
    position: absolute;
    left: 30px;
    top: 420px;
    font-family: "Open Sans", sans-serif;
    font-style: italic;
    color: var(--ink-grey);
    line-height: 1.5;
  }
  .claim-lead { display: block; font-size: 24px; }
  .claim-follow { display: block; font-size: 20px; }
  .classic-hair {
    position: absolute;
    left: 30px;
    top: 540px;
    font-family: "Marcellus", serif;
    font-size: 20px;
    color: var(--ink-grey);
  }
  .classic-free {
    position: absolute;
    left: 30px;
    top: 574px;
    font-family: "Open Sans", sans-serif;
    font-size: 13px;
    color: var(--ink-soft);
  }
  .classic-volume {
    position: absolute;
    right: 26px;
    top: 632px;
    font-family: "Open Sans", sans-serif;
    font-size: 9px;
    color: var(--ink-soft);
  }
  .classic-foliage {
    position: absolute;
    left: 0;
    right: 0;
    top: 672px;
    bottom: 0;
    background:
      radial-gradient(ellipse at 30% 40%, var(--leaf-light) 0%, transparent 55%),
      radial-gradient(ellipse at 75% 65%, var(--leaf-dark) 0%, transparent 60%),
      linear-gradient(160deg, var(--leaf-light), var(--leaf-green) 60%, var(--leaf-dark));
    opacity: 0.85;
  }

  /* fresh label */
  .fresh-title {
    position: absolute;
    right: 30px;
    top: 214px;
    font-family: "Arapey", serif;
    font-size: 76px;
    color: var(--ink-dark);
    line-height: 1;
    white-space: nowrap;
  }
  .fresh-sub {
    position: absolute;
    right: 32px;
    top: 306px;
    font-family: "Poiret One", sans-serif;
    font-size: 50px;
    color: var(--leaf-green);
    line-height: 1;
  }
  .fresh-claim {
    position: absolute;
    right: 32px;
    top: 412px;
    text-align: right;
    font-family: "Open Sans", sans-serif;
    font-style: italic;
    color: var(--leaf-green);
    line-height: 1.4;
  }
  .fresh-hair {
    position: absolute;
    right: 32px;
    top: 482px;
    font-family: "Marcellus", serif;
    font-size: 14px;
    color: var(--leaf-dark);
  }
  .fresh-foliage {
    position: absolute;
    left: 0;
    top: 528px;
    width: 330px;
    height: 410px;
    border-radius: 0 60% 40% 0;
    background:
      radial-gradient(ellipse at 70% 55%, var(--leaf-light) 0%, transparent 55%),
      radial-gradient(ellipse at 20% 70%, var(--leaf-dark) 0%, transparent 60%),
      linear-gradient(140deg, var(--leaf-green), var(--leaf-light) 55%, var(--leaf-green));
    opacity: 0.85;
  }
  .fresh-seal {
    position: absolute;
    left: 276px;
    top: 520px;
    width: 84px;
    height: 84px;
    border-radius: 50%;
    border: 3px solid var(--leaf-green);
    background: var(--label);
    box-sizing: border-box;
  }
  .fresh-volume {
    position: absolute;
    right: 30px;
    top: 960px;
    font-family: "Open Sans", sans-serif;
    font-style: italic;
    font-size: 16px;
    color: var(--leaf-green);
  }
</style>
</head>
<body>
<main class="canvas">

  <section class="label label--classic">
    <div class="brand"><span class="brand-dot"></span><span class="brand-name">Venoro</span></div>
    <h1 class="classic-title">SHAMPOO</h1>
    <div class="rule"></div>
    <p class="classic-sub">ORGANIC</p>
    <p class="classic-claim">
      <span class="claim-lead">smooth, shiny</span>
      <span class="claim-follow">touchable , soft results</span>
    </p>
    <p class="classic-hair">FOR NORMAL TO DRY HAIR</p>
    <p class="classic-free">Chemical Free *Cruelty Free *Consern Free</p>
    <p class="classic-volume">250 ML / 8.8 FL.OZ</p>
    <div class="classic-foliage" role="img" aria-label="Pattern of scattered light and dark green leafy branches"></div>
  </section>

  <section class="label label--fresh">
    <div class="brand"><span class="brand-dot"></span><span class="brand-name">Venoro</span></div>
    <h1 class="fresh-title">shampoo</h1>
    <div class="rule"></div>
    <p class="fresh-sub">organic</p>
    <p class="fresh-claim">
      <span class="claim-lead">smooth, shiny</span>
      <span class="claim-follow">touchable , soft results</span>
    </p>
    <p class="fresh-hair">for normal to dry hair</p>
    <div class="fresh-foliage" role="img" aria-label="Illustration of large overlapping fresh green leaves"></div>
    <div class="fresh-seal" aria-hidden="true"></div>
    <p class="fresh-volume">250 ml / 8,8 fl.oz</p>
  </section>

</main>
</body>
</html>
```